Yard sign design for high end luxury home builder.

Need a design for signage on custom homes that are being built. I already have a logo that I am satisfied with that needs to be incorporated. I need the following incorporated in the design of the sign-
- Lic number 318562
- phone number (555) 271-4038
- pendrickhomeworks.com
- Logo/Branding

If possible it may be nice to have the following quote that is on are business cards-

Quote from Osmund of Veltarra-
HE WHO WORKS WITH HIS HANDS IS A LABORER.
HE WHO WORKS WITH HIS HANDS & HIS HEAD IS A CRAFTSMAN.
HE WHO WORKS WITH HIS HANDS & HIS HEAD & HIS HEART IS AN ARTISAN.
-OSMUND OF VELTARRA

Target Market(s)

Archetect, Designers, Clients desiring to build a new home or remodel.

Colors
fde9d4
fee4d5
fabb94
fac994
faa54b
f68d4d
f37122
f78f20
f68e4e

Requirements
Must have
• - Lic number 318562
• - phone number (555) 271-4038
• - pendrickhomeworks.com
• - Logo/Branding
Nice to have
• Quote from Osmund of Veltarra-
• HE WHO WORKS WITH HIS HANDS IS A LABORER.
• HE WHO WORKS WITH HIS HANDS & HIS HEAD IS A CRAFTSMAN.
• HE WHO WORKS WITH HIS HANDS & HIS HEAD & HIS HEART IS AN ARTISAN.
• -OSMUND OF VELTARRA
• OR the below statement-
• Craftsmen that Care
Should not have
• Any additional verbiage not specified above including any type of verbiage about what kind of company we are. For instance- Integrity, reputable... It's just all played out. Im just looking for a bitching design that has the info that compliments my logo/branding.

```html
<!DOCTYPE html>
<html lang="en">
<head>
<meta charset="utf-8">
<title>Pendrick Homeworks Yard Sign</title>
<link rel="stylesheet" href="https://fonts.googleapis.com/css2?family=Oswald:wght@500;600&display=swap">
<style>
  :root {
    --orange: #f68d4d;
    --white: #ffffff;
    --ink: #111111;
    --wood-dark: #5f4c3a;
    --wood-mid: #7a6551;
    --wood-light: #8c7862;
    --brand: #8a7560;
  }
  html, body {
    margin: 0;
    padding: 0;
    overflow: hidden;
    background: var(--white);
  }
  .sign {
    position: relative;
    width: 1200px;
    height: 900px;
    overflow: hidden;
    background: var(--white);
    font-family: "Oswald", "Arial Narrow", sans-serif;
  }
  .shapes {
    position: absolute;
    inset: 0;
  }
  .wood-panel {
    position: absolute;
    left: 0;
    top: 126px;
    width: 1200px;
    height: 645px;
    background: linear-gradient(175deg, var(--wood-light) 0%, var(--wood-mid) 40%, var(--wood-dark) 75%, var(--wood-mid) 100%);
  }
  .brand-box {
    position: absolute;
    left: 34px;
    top: 39px;
    width: 249px;
    height: 183px;
    background: var(--white);
    display: flex;
    flex-direction: column;
    align-items: center;
    justify-content: center;
    gap: 14px;
  }
  .brand-mark {
    width: 60px;
    height: 60px;
    background: var(--brand);
  }
  .brand-name {
    margin: 0;
    color: var(--brand);
    font-weight: 600;
    font-size: 22px;
    line-height: 1.1;
    letter-spacing: 1px;
    text-align: center;
  }
  .quote-list {
    position: absolute;
    left: 82px;
    top: 232px;
    margin: 0;
    padding: 0;
    list-style: none;
  }
  .quote-list li {
    position: relative;
    padding-left: 40px;
    height: 74px;
    color: var(--white);
    font-weight: 600;
    font-size: 35px;
    line-height: 44px;
    text-shadow: 1px 2px 2px rgba(0,0,0,0.55);
  }
  .quote-list li::before {
    content: "";
    position: absolute;
    left: 0;
    top: 15px;
    width: 15px;
    height: 15px;
    background: var(--white);
  }
  .phone {
    position: absolute;
    right: 30px;
    top: 645px;
    margin: 0;
    color: var(--white);
    font-weight: 500;
    font-size: 92px;
    line-height: 1;
    letter-spacing: 1px;
  }
  .website {
    position: absolute;
    left: 74px;
    top: 803px;
    margin: 0;
    color: var(--ink);
    font-weight: 600;
    font-size: 44px;
    line-height: 1;
  }
  .licence {
    position: absolute;
    left: 680px;
    top: 790px;
    width: 500px;
    margin: 0;
    text-align: center;
    color: var(--ink);
    font-weight: 600;
    font-size: 58px;
    line-height: 1;
  }
</style>
</head>
<body>
<main class="sign">
  <div class="wood-panel" role="img" aria-label="Weathered wood plank texture background"></div>
  <svg class="shapes" width="1200" height="900" viewBox="0 0 1200 900" aria-hidden="true">
    <polygon points="655,0 1200,0 1200,90 591,90" fill="var(--orange)"/>
    <rect x="0" y="771" width="1200" height="129" fill="var(--orange)"/>
    <polygon points="660,771 1200,771 1200,868 591,868" fill="var(--white)"/>
  </svg>

  <div class="brand-box">
    <div class="brand-mark"></div>
    <p class="brand-name">PENDRICK HOMEWORKS INC.</p>
  </div>

  <ul class="quote-list">
    <li>Quote from Osmund of Veltarra-</li>
    <li>HE WHO WORKS WITH HIS HANDS IS A LABORER.</li>
    <li>HE WHO WORKS WITH HIS HANDS &amp; HIS HEAD IS A CRAFTSMAN.</li>
    <li>HE WHO WORKS WITH HIS HANDS &amp; HIS HEAD &amp; HIS HEART IS AN ARTISAN.</li>
    <li>OSMUND OF VELTARRA</li>
    <li>the below statement</li>
    <li>Craftsmen that Care</li>
  </ul>

  <p class="phone">(555) 271-4038</p>
  <p class="website">www.pendrickhomeworks.com</p>
  <p class="licence">Lic number 318562</p>
</main>
</body>
</html>
```